Looking for a high-end business card design for a construction company

We are looking to update our business card design. We are a post-frame construction company that builds custom buildings, commercial spaces, homes, and anything else. We have multiple people working here so we would need something we can easily customize the information for the specific person. We need a name, website, cell phone, office phone as well as social icons. Our colors are black, white, and grey/silver so I would love a black background or something that is more striking than just a traditional white business card. Looking for something that is very professional with a high-end look/feel. I have attached our logos, they can be silver, white, grey, or black.
Industry/Entity Type
Construction
Contact Information for Business Card
Business logo, Name, Cell phone, Office phone, website, social Icons
Colors
Designer to choose only greyscale colors for use in the design.
Look and feel

```html
<!DOCTYPE html>
<html lang="en">
<head>
<meta charset="utf-8">
<title>Harrowgate Builders – Business Card</title>
<link href="https://fonts.googleapis.com/css2?family=Montserrat:wght@400;500;700&display=swap" rel="stylesheet">
<style>
  :root {
    --backdrop: #cbcfcf;
    --card: #ffffff;
    --ink: #111111;
    --silver: #8a8a8a;
    --light-silver: #d6d6d6;
    --shadow: rgba(0,0,0,0.22);
  }
  * { margin: 0; padding: 0; box-sizing: border-box; }
  html, body { width: 1200px; height: 1059px; overflow: hidden; }
  body {
    background: var(--backdrop);
    font-family: 'Montserrat', sans-serif;
    color: var(--ink);
    position: relative;
  }
  .card {
    position: absolute;
    left: 220px;
    width: 760px;
    height: 434px;
    background: var(--card);
    box-shadow: 0 14px 30px var(--shadow);
    overflow: hidden;
  }
  .card--front { top: 70px; }
  .card--back  { top: 555px; background: var(--ink); }

  .card__wave { position: absolute; inset: 0; width: 100%; height: 100%; }

  .brand {
    position: absolute;
    display: flex;
    align-items: center;
    gap: 18px;
    font-weight: 700;
    color: var(--ink);
    text-transform: uppercase;
  }
  .brand__dot {
    width: 54px; height: 54px;
    border-radius: 50%;
    background: currentColor;
    flex: none;
  }
  .brand__name { line-height: 0.95; }
  .brand__primary { display: block; font-size: 46px; letter-spacing: 4px; }
  .brand__secondary { display: block; font-size: 24px; letter-spacing: 5px; padding-left: 4px; }

  .card--front .brand { top: 52px; left: 170px; }
  .card--back .brand { top: 165px; left: 50%; transform: translateX(-50%); color: var(--card); }

  .person {
    position: absolute;
    top: 172px;
    right: 430px;
    text-align: right;
  }
  .person__name { font-size: 24px; font-weight: 700; letter-spacing: 0.3px; }
  .person__title { font-size: 14px; font-weight: 400; margin-top: 4px; }

  .divider {
    position: absolute;
    left: 346px;
    top: 172px;
    width: 2px;
    height: 92px;
    background: var(--ink);
  }

  .contacts {
    position: absolute;
    left: 366px;
    top: 174px;
    list-style: none;
    font-size: 19px;
    font-weight: 400;
  }
  .contacts li { display: flex; align-items: center; gap: 10px; height: 30px; }
  .contacts svg { width: 17px; height: 17px; fill: var(--ink); flex: none; }

  .address {
    position: absolute;
    left: 170px;
    top: 282px;
    font-size: 19px;
    font-weight: 400;
  }

  .social {
    position: absolute;
    left: 40px;
    bottom: 28px;
    display: flex;
    gap: 14px;
    list-style: none;
  }
  .social li {
    width: 30px; height: 30px;
    border-radius: 50%;
    background: var(--light-silver);
  }
</style>
</head>
<body>

<section class="card card--front" aria-label="Business card front">
  <svg class="card__wave" viewBox="0 0 760 434" preserveAspectRatio="none" aria-hidden="true">
    <path d="M0,215 C40,290 110,330 290,338 C470,346 610,376 760,426 L760,434 L0,434 Z" fill="#8a8a8a"/>
    <path d="M0,236 C45,312 120,352 300,360 C480,368 620,394 740,434 L0,434 Z" fill="#111111"/>
  </svg>

  <div class="brand">
    <span class="brand__dot"></span>
    <span class="brand__name">
      <span class="brand__primary">Harrowgate</span>
      <span class="brand__secondary">Builders, Inc.</span>
    </span>
  </div>

  <div class="person">
    <p class="person__name">DECLAN MARSH</p>
    <p class="person__title">Director of Business Development</p>
  </div>

  <span class="divider"></span>

  <ul class="contacts">
    <li>
      <svg viewBox="0 0 24 24" aria-hidden="true"><path d="M6.6 10.8a15.1 15.1 0 0 0 6.6 6.6l2.2-2.2a1 1 0 0 1 1-.25 11.4 11.4 0 0 0 3.6.57 1 1 0 0 1 1 1V20a1 1 0 0 1-1 1A17 17 0 0 1 3 4a1 1 0 0 1 1-1h3.5a1 1 0 0 1 1 1c0 1.250.2 2.450.57 3.57a1 1 0 0 1-.25 1z"/></svg>
      <span>555 214 7730</span>
    </li>
    <li>
      <svg viewBox="0 0 24 24" aria-hidden="true"><path d="M2 8c3-4 17-4 20 0l-1 3h-4l-1-2H8L7 11H3zM6 12h12l2 8H4zm6 2a2.5 2.5 0 1 0 0 5 2.5 2.5 0 0 0 0-5z"/></svg>
      <span>555-380-1946</span>
    </li>
    <li>
      <svg viewBox="0 0 24 24" aria-hidden="true"><path d="M12 2a10 10 0 1 0 0 20 10 10 0 0 0 0-20zm-1 17.9A8 8 0 0 1 4.1 11H7a14 14 0 0 0 4 8.9zM13 4.1A8 8 0 0 1 19.9 11H17a14 14 0 0 0-4-6.9zM9 11a12 12 0 0 1 3-6.8A12 12 0 0 1 15 11zm3 8.8A12 12 0 0 1 9 13h6a12 12 0 0 1-3 6.8z"/></svg>
      <span>www.harrowgatebuild.com</span>
    </li>
  </ul>

  <p class="address">2280 Quarry Lane Suite 410 Elmfield, CA 955</p>

  <ul class="social" aria-label="Social profiles">
    <li aria-label="Social profile"></li>
    <li aria-label="Social profile"></li>
    <li aria-label="Social profile"></li>
    <li aria-label="Social profile"></li>
  </ul>
</section>

<section class="card card--back" aria-label="Business card back">
  <div class="brand">
    <span class="brand__dot"></span>
    <span class="brand__name">
      <span class="brand__primary">Harrowgate</span>
      <span class="brand__secondary">Builders, Inc.</span>
    </span>
  </div>
</section>

</body>
</html>
```